Brightmoor Business Solutions

I need a business card design with logo for my business and management consultancy business. I am based in Singapore and I provide (i) accounting / bookkeeping services; (ii) management and business consultancy solutions; (iii) tax advisory and consultancy; and (iv) risk management and corporate governance. I want the design to be bold and outstanding yet doesn't give the impression that I take unnecessary risks.

Reason: To the designers who have gotten messages from me, I'm still waiting for some changes to be made.

Target Market(s)

Small to large enterprises which are willing to pay value for money and not necessarily the cheapest

Industry/Entity Type

Accounting

Contact Information for Business Card

Name, email address and mobile no.

Requirements
Must have
• If possible, could you incorporate the Sigma symbol as the E for Brightmoor or the Equals sign to show that the business relates to finance / financials and that I provide solutions which may it easy for my clients.
Should not have
• Black / dark backgrounds

```html
<!DOCTYPE html>
<html lang="en">
<head>
<meta charset="utf-8">
<title>Brightmoor Business Solutions — Business Card</title>
<link rel="stylesheet" href="https://fonts.googleapis.com/css2?family=Libre+Baskerville:wght@400;700&display=swap">
<style>
  :root {
    --page-bg: #e4e4e4;
    --card-white: #ffffff;
    --brand-blue: #233e8b;
    --text-white: #ffffff;
  }
  html, body {
    margin: 0;
    padding: 0;
    width: 1200px;
    height: 900px;
    overflow: hidden;
    background: var(--page-bg);
  }
  .card {
    position: absolute;
    left: 150px;
    top: 193px;
    width: 900px;
    height: 514px;
    background: var(--card-white);
    box-shadow: 0 6px 18px rgba(0, 0, 0, 0.18);
    overflow: hidden;
    font-family: "Libre Baskerville", "Times New Roman", serif;
  }
  .card-bands {
    position: absolute;
    inset: 0;
    width: 900px;
    height: 514px;
  }
  .brand {
    position: absolute;
    left: 0;
    top: 168px;
    width: 820px;
    display: flex;
    justify-content: center;
    align-items: center;
    gap: 12px;
  }
  .brand-mark {
    width: 16px;
    height: 16px;
    background: var(--brand-blue);
  }
  .brand-name {
    margin: 0;
    font-size: 27px;
    font-weight: 700;
    color: var(--brand-blue);
    letter-spacing: 0.5px;
  }
  .contact {
    position: absolute;
    right: 42px;
    margin: 0;
    font-size: 24px;
    font-weight: 400;
    color: var(--text-white);
    letter-spacing: 0.5px;
  }
  .contact-phone { top: 254px; }
  .contact-email { top: 322px; }
  .holder-name {
    position: absolute;
    left: 78px;
    top: 430px;
    margin: 0;
    font-size: 25px;
    font-weight: 400;
    color: var(--text-white);
  }
</style>
</head>
<body>
  <article class="card">
    <svg class="card-bands" viewBox="0 0 900 514" aria-hidden="true">
      <!-- left name panel -->
      <polygon fill="var(--brand-blue)" points="0,330 440,330 592,514 0,514"/>
      <!-- right contact panel -->
      <polygon fill="var(--brand-blue)" points="430,240 900,240 900,514 624,514"/>
      <!-- contact band dividers -->
      <rect fill="var(--card-white)" x="400" y="302" width="500" height="7"/>
      <rect fill="var(--card-white)" x="400" y="370" width="500" height="7"/>
    </svg>

    <div class="brand">
      <span class="brand-mark"></span>
      <h1 class="brand-name">Brightmoor Business Solutions</h1>
    </div>

    <p class="contact contact-phone">+65-8100 5523</p>
    <p class="contact contact-email">jlee.bms@mailbox.com</p>

    <p class="holder-name">Your Name</p>
  </article>
</body>
</html>
```